The Best Real Estate Post Card Ever

Create a memorable and attention grabbing postcard BACK to be used the same every month and sent to 20,000 homes. The front of the postcard will change, I will make this every month. But the back I want to be known as ME and when people see it after years they instantly think of ME. This is all about branding and getting to be known as the agent to call when they need to move. I have attached styles I have used on past marketing. This design must work with both 11x8.5 and 9x6 and allow room for the postage to flow nicely.

Target Market(s)

Luxury waterfront clients

Colors
ec1f27
0255a3
ffffff

Requirements
Must have
• Clean and modern, luxury feel to it.
Nice to have
• Attention grabbing way to be remembered.
Should not have
• cheap look

```html
<!DOCTYPE html>
<html lang="en">
<head>
<meta charset="utf-8">
<title>Owen Castellan – Postcard Backs</title>
<link href="https://fonts.googleapis.com/css2?family=Cinzel:wght@400;600;700&family=Great+Vibes&family=Open+Sans:ital,wght@0,400;0,600;1,600&display=swap" rel="stylesheet">
<style>
:root{
  --navy:#123566;
  --navy-deep:#0c2a55;
  --red:#b8102f;
  --white:#ffffff;
  --ink:#2a2a2a;
  --grey:#4a4a4a;
  --page:#efefef;
}
*{margin:0;padding:0;box-sizing:border-box}
html,body{width:890px;height:1200px;overflow:hidden;background:var(--page)}
.stage{position:absolute;left:0;top:0;width:1093px;height:1473px;transform:scale(.81427);transform-origin:0 0}
.card{position:absolute;left:151px;width:792px;height:612px;overflow:hidden;background:var(--white);box-shadow:0 4px 24px rgba(0,0,0,.18)}
.card--front{top:80px}
.card--back{top:781px}
.abs{position:absolute}
.serif{font-family:"Cinzel",serif}
.sans{font-family:"Open Sans",sans-serif}

/* brand seal stand-in */
.seal{position:absolute;display:flex;flex-direction:column;align-items:center;justify-content:center;border-radius:50%;text-align:center;font-family:"Cinzel",serif;font-weight:600}
.seal__name{font-size:17px;line-height:1.1}
.seal__sub{font-size:9px;margin-top:3px;letter-spacing:.5px}

/* front */
.front-seal{left:28px;top:8px;width:112px;height:112px;border:3px solid var(--red);color:var(--navy)}
.agent-name{font-family:"Cinzel",serif;font-weight:700;color:var(--ink)}
.front-name{left:177px;top:18px;font-size:22px}
.front-creds{left:177px;top:45px;font-family:"Cinzel",serif;font-size:15px;color:var(--grey)}
.front-title{left:175px;top:74px;font-family:"Open Sans",sans-serif;font-style:italic;font-weight:600;font-size:15.5px;line-height:23px;color:var(--grey)}
.banner-text{left:495px;top:10px;width:297px;text-align:center;color:var(--white);font-family:"Cinzel",serif}
.banner-text__small{font-size:17px;letter-spacing:.5px}
.banner-text__big{font-size:33px;font-weight:700;line-height:1.05}
.perks{left:498px;top:96px;width:290px;list-style:none}
.perk{position:absolute;left:0;display:flex;align-items:flex-start;gap:14px;color:var(--white);font-family:"Open Sans",sans-serif;font-size:13.5px;line-height:14px}
.perk svg{flex:0 0 36px;width:36px;height:36px;margin-top:-6px}
.postage-box{left:529px;top:450px;width:246px;height:149px;background:var(--white)}
.name-tag{left:22px;top:463px;color:var(--white)}
.name-tag__name{font-family:"Cinzel",serif;font-weight:600;font-size:22px}
.name-tag__creds{font-family:"Cinzel",serif;font-size:12.5px;margin-top:2px}
.contact{display:flex;align-items:center;gap:6px;font-family:"Open Sans",sans-serif;font-size:16px;color:var(--grey)}
.contact svg{width:27px;height:27px}

/* back */
.back-seal{left:35px;top:10px;width:118px;height:118px;border:3px solid var(--white);color:var(--white)}
.back-name{left:182px;top:38px;font-size:28px;color:var(--white)}
.back-creds{left:182px;top:70px;font-family:"Cinzel",serif;font-size:20px;color:var(--white)}
.back-title{left:505px;top:36px;font-family:"Open Sans",sans-serif;font-style:italic;font-weight:600;font-size:20px;line-height:30px;color:var(--white)}
.tagline{font-family:"Great Vibes",cursive;font-size:42px;color:var(--white);line-height:1}
.brand-mark{left:320px;top:412px;width:154px;display:flex;align-items:center;justify-content:center;gap:6px;font-family:"Open Sans",sans-serif;font-weight:600;font-size:17px;color:var(--navy)}
.brand-mark__dot{width:14px;height:14px;border-radius:50%;background:var(--red)}
.back-sign{left:0;top:497px;width:792px;text-align:center}
.back-sign__name{font-family:"Cinzel",serif;font-size:31px;color:var(--ink)}
.back-sign__creds{font-family:"Cinzel",serif;font-size:16px;color:var(--ink);margin-top:2px}
.back-contacts{left:0;top:565px;width:792px;display:flex;justify-content:center;gap:16px}
.back-contacts .contact{font-size:18px;color:var(--ink)}
.back-contacts .contact svg{width:32px;height:32px}
</style>
</head>
<body>
<div class="stage">

  <!-- Postcard front-facing back: perks layout -->
  <section class="card card--front">
    <svg class="abs" style="left:0;top:0" width="792" height="612" viewBox="0 0 792 612">
      <polygon points="376,300 500,612 513,612 386,300" fill="var(--red)"/>
      <polygon points="495,40 792,40 792,612 512,612 379,295" fill="var(--navy)"/>
      <polygon points="495,0 792,0 792,60 643,72 495,60" fill="var(--red)"/>
      <polygon points="0,456 262,456 295,521 0,521" fill="var(--navy)"/>
    </svg>

    <div class="seal front-seal"><span class="seal__name">OWEN<br>CASTELLAN</span><span class="seal__sub" style="color:var(--red)">HARBORLINE PALM</span></div>
    <div class="abs agent-name front-name">OWEN CASTELLAN,</div>
    <div class="abs front-creds">CRS, ABR, SRS, PSA</div>
    <div class="abs front-title">Realtor | Broker Associate -<br>Harborline Palm Realty</div>

    <div class="abs banner-text"><div class="banner-text__small">RESULTS THAT</div><div class="banner-text__big">MOVE YOU</div></div>

    <ul class="abs perks">
      <li class="perk" style="top:10px"><svg viewBox="0 0 36 36" fill="var(--white)"><path d="M14 16h3l3-7c2 0 2 2 2 4l-1 3h5c1 0 2 1 2 2l-2 7c0 1-1 2-2 2h-10z"/><rect x="10" y="16" width="3" height="11"/><circle cx="4" cy="16" r="1.6"/><circle cx="8" cy="6" r="1.6"/><circle cx="18" cy="2" r="1.6"/><circle cx="28" cy="6" r="1.6"/><circle cx="32" cy="16" r="1.6"/><circle cx="8" cy="30" r="1.6"/><circle cx="28" cy="30" r="1.6"/></svg><span>200+ 5 star online reviews.</span></li>
      <li class="perk" style="top:38px"><svg viewBox="0 0 36 36" fill="none" stroke="var(--white)" stroke-width="2.4"><path d="M18 28c-6-8-8-11-8-15a8 8 0 0 1 16 0c0 4-2 7-8 15z"/><circle cx="18" cy="13" r="3"/><ellipse cx="18" cy="31" rx="9" ry="2.5"/></svg><span>Charlotte county resident<br>20+ years.</span></li>
      <li class="perk" style="top:80px"><svg viewBox="0 0 36 36" fill="none" stroke="var(--white)" stroke-width="2.2"><path d="M4 16 18 5l14 11"/><rect x="7" y="16" width="22" height="16"/><rect x="15" y="23" width="6" height="9"/><rect x="10" y="19" width="3" height="3"/><rect x="23" y="19" width="3" height="3"/></svg><span>Certified luxury home<br>marketing specialist.</span></li>
      <li class="perk" style="top:122px"><svg viewBox="0 0 36 36" fill="none" stroke="var(--white)" stroke-width="2.2"><rect x="3" y="6" width="26" height="24" rx="2"/><path d="M3 12h26M9 3v6M23 3v6"/><circle cx="28" cy="28" r="6" fill="var(--navy)"/><path d="m25 28 2 2 4-4"/></svg><span>Available 7 days a week<br>from 8am till midnight.</span></li>
      <li class="perk" style="top:164px"><svg viewBox="0 0 36 36" fill="var(--white)"><path d="M3 15 18 4l15 11-2 2L18 7 5 17z"/><circle cx="18" cy="17" r="4"/><path d="M10 32c0-6 3-9 8-9s8 3 8 9z"/></svg><span>Top 1% of realtors as ranked by<br>volume by local board of realtors</span></li>
      <li class="perk" style="top:206px"><svg viewBox="0 0 36 36" fill="var(--white)"><rect x="9" y="4" width="10" height="7" rx="1"/><rect x="4" y="11" width="28" height="20" rx="2"/><circle cx="18" cy="21" r="6" fill="var(--navy)"/><circle cx="18" cy="21" r="3.5"/></svg><span>Professional photography<br>included with every listing.</span></li>
      <li class="perk" style="top:248px"><svg viewBox="0 0 36 36" fill="none" stroke="var(--white)" stroke-width="2.2"><path d="M22 32H6V6h20v8"/><path d="M10 12h12M10 17h10M10 22h6"/><path d="m18 27 12-12 3 3-12 12h-3z"/></svg><span>Hassle free listing agreements,<br>cancel anytime with no fees.</span></li>
      <li class="perk" style="top:290px"><svg viewBox="0 0 36 36" fill="var(--white)"><circle cx="14" cy="11" r="6"/><path d="M3 32c0-8 5-12 11-12 3 0 5 1 7 2v10z"/><circle cx="27" cy="25" r="7"/><path d="m27 20 1.5 3h3l-2.5 2 1 3-3-2-3 2 1-3-2.5-2h3z" fill="var(--navy)"/></svg><span>5 star guarantee- ifs don’t<br>meet your expectations, you<br>don’t pay me.</span></li>
    </ul>

    <div class="abs" role="img" aria-label="Photograph of the agent smiling and holding his young son" style="left:290px;top:395px;width:214px;height:217px;border-radius:90px 90px 0 0;background:linear-gradient(180deg,#c9a98d 0%,#7b7d83 45%,#5b5e64 100%)"></div>

    <div class="abs postage-box"></div>

    <div class="abs name-tag"><div class="name-tag__name">OWEN CASTELLAN,</div><div class="name-tag__creds">CRS, ABR, SRS, PSA, CLHMS, SFR, RSPS</div></div>

    <div class="abs contact" style="left:21px;top:531px"><svg viewBox="0 0 28 28"><circle cx="14" cy="14" r="14" fill="var(--red)"/><path d="M9 7c1 0 2 3 2 4l-1.5 1.5c1 2 3 4 5 5L16 16c1 0 4 1 4 2 0 1.5-1.5 3-3 3-5 0-10-5-10-10 0-1.5 1.5-4 2-4z" fill="var(--white)"/></svg>(555) 014 - 2288</div>
    <div class="abs contact" style="left:21px;top:569px"><svg viewBox="0 0 28 28"><circle cx="14" cy="14" r="14" fill="var(--red)"/><rect x="7" y="9" width="14" height="10" rx="1" fill="var(--white)"/><path d="m7 10 7 5 7-5" fill="none" stroke="var(--red)" stroke-width="1.4"/></svg>OwenCastellan@Harborline.net</div>
  </section>

  <!-- Postcard back: home scene layout -->
  <section class="card card--back">
    <div class="abs" role="img" aria-label="Dusk photograph of a stone-front waterfront home with a wooden garage door, palm trees and a paver driveway" style="left:0;top:0;width:792px;height:612px;background:linear-gradient(180deg,#4d5260 0%,#8a7a6e 18%,#3d4250 32%,#6b6f70 48%,#4f6a3c 70%,#8b8a86 100%)"></div>
    <div class="abs" role="img" aria-label="Photograph of the agent smiling and holding his young son" style="left:5px;top:180px;width:300px;height:400px;border-radius:140px 140px 0 0;background:linear-gradient(180deg,#c7a283 0%,#6e7177 45%,#55585e 100%)"></div>

    <svg class="abs" style="left:0;top:0" width="792" height="612" viewBox="0 0 792 612">
      <polygon points="0,612 0,583 149,445 205,500 397,335 500,425 515,425 635,445 792,583 792,612" fill="var(--white)"/>
      <polygon points="0,566 149,437 218,500 205,513 149,461 0,594" fill="var(--red)"/>
      <polygon points="792,566 642,437 575,496 588,510 642,461 792,594" fill="var(--red)"/>
      <polygon points="147,559 397,324 471,394 471,369 517,369 517,437 646,559 628,559 397,350 166,559" fill="var(--navy-deep)"/>
    </svg>

    <div class="seal back-seal"><span class="seal__name">OWEN<br>CASTELLAN</span><span class="seal__sub">HARBORLINE PALM</span></div>
    <div class="abs agent-name back-name">OWEN CASTELLAN,</div>
    <div class="abs back-creds">CRS, ABR, SRS, PSA</div>
    <div class="abs back-title">Realtor | Broker Associate -<br>Harborline Palm Realty</div>

    <div class="abs tagline" style="left:475px;top:283px">Better Services</div>
    <div class="abs tagline" style="left:517px;top:330px">Better Marketing</div>
    <div class="abs tagline" style="left:558px;top:378px">Better Results</div>

    <div class="abs brand-mark"><span class="brand-mark__dot"></span>Harborline</div>

    <div class="abs back-sign"><div class="back-sign__name">OWEN CASTELLAN</div><div class="back-sign__creds">CRS, ABR, SRS, PSA, CLHMS, SFR, RSPS</div></div>

    <div class="abs back-contacts">
      <div class="contact"><svg viewBox="0 0 28 28"><circle cx="14" cy="14" r="14" fill="var(--red)"/><path d="M9 7c1 0 2 3 2 4l-1.5 1.5c1 2 3 4 5 5L16 16c1 0 4 1 4 2 0 1.5-1.5 3-3 3-5 0-10-5-10-10 0-1.5 1.5-4 2-4z" fill="var(--white)"/></svg>(555) 014 - 2288</div>
      <div class="contact"><svg viewBox="0 0 28 28"><circle cx="14" cy="14" r="14" fill="var(--red)"/><rect x="7" y="9" width="14" height="10" rx="1" fill="var(--white)"/><path d="m7 10 7 5 7-5" fill="none" stroke="var(--red)" stroke-width="1.4"/></svg>OwenCastellan@Harborline.net</div>
    </div>
  </section>

</div>
</body>
</html>
```